Website for Apartment Rental in Prague

I would like to create designs of my website focused on luxury apartment rentals in Prague, Czech Republic. I created initial mock-ups, They are all attached. I need to design homepage and subpage. The mock-ups were created by combining elements from different websites that I liked but I need you to create a design that is unique and original. The attached files a only a guidance for the structure of the website but not for the design. Try to be creative.

Industry/Entity Type

Apartment

```html
<!DOCTYPE html>
<html lang="en">
<head>
<meta charset="utf-8">
<title>Belvue Apartments Prague</title>
<link href="https://fonts.googleapis.com/css2?family=Montserrat:wght@300;400;500;600;700;800&display=swap" rel="stylesheet">
<style>
  :root{
    --backdrop:#f2f2f2;
    --page:#ffffff;
    --ink:#222222;
    --ink-soft:#444444;
    --sidebar:#2a2a2a;
    --muted:#8a8a8a;
    --gold:#e6bf36;
    --field-line:#c9c9c9;
    --panel-dark:rgba(30,30,30,.88);
  }
  *{box-sizing:border-box;margin:0;padding:0}
  html,body{width:1200px;height:1200px;overflow:hidden}
  body{background:var(--backdrop);font-family:"Montserrat",Arial,sans-serif;color:var(--ink);position:relative}
  .page{position:absolute;left:238px;top:0;width:738px;height:1200px;background:var(--backdrop);box-shadow:0 0 40px rgba(0,0,0,.05)}

  .hero-photo{position:absolute;left:451px;top:0;width:525px;height:348px;
    background:
      radial-gradient(ellipse at 80% 10%,rgba(255,255,255,.7),transparent 45%),
      linear-gradient(180deg,#d9d9dc 0%,#a8a7a8 45%,#6f6a66 70%,#8d8885 100%)}

  .sidebar{position:absolute;left:238px;top:0;width:213px;height:339px;background:var(--sidebar)}
  .brand{position:absolute;left:66px;top:28px;display:flex;align-items:center;gap:7px}
  .brand-mark{width:7px;height:7px;background:#fff}
  .brand-name{font-weight:600;font-size:10.5px;letter-spacing:.5px;color:#fff;white-space:nowrap}
  .main-nav{position:absolute;left:70px;top:80px;list-style:none}
  .main-nav li{height:20.4px;display:flex;align-items:center;font-size:8.2px;color:#fff;letter-spacing:.2px;position:relative;padding-left:13px}
  .main-nav li::before{content:"";position:absolute;left:1px;top:8px;width:4px;height:4px;background:#fff;transform:rotate(45deg)}
  .main-nav li.active{color:var(--gold);font-weight:700}
  .main-nav li.active::before{left:-1px;top:6px;width:7px;height:7px;background:transparent;border:1.5px solid var(--gold);box-shadow:inset 0 0 0 1.5px var(--sidebar),inset 0 0 0 4px var(--gold)}
  .sidebar-heading{position:absolute;left:66px;top:281px;font-size:12px;font-weight:700;color:#8e8e8e;letter-spacing:.3px}

  .discover{position:absolute;left:818px;top:22px;width:158px;height:25px;background:var(--gold);color:#fff;font-size:8.5px;font-weight:700;display:flex;align-items:center;padding-left:14px;letter-spacing:.3px}

  .booking-head{position:absolute;left:542px;top:85px;width:368px;height:81px;background:var(--panel-dark)}
  .booking-head h1{position:absolute;right:12px;top:10px;text-align:right;font-size:26px;line-height:28px;font-weight:700;color:#fff;letter-spacing:.3px}
  .booking-head .label{position:absolute;left:12px;bottom:4px;font-size:9px;font-weight:700;color:#fff}
  .booking-form{position:absolute;left:542px;top:166px;width:291px;height:103px;background:#fff}
  .field-label{position:absolute;font-size:5.5px;font-weight:600;color:var(--gold);letter-spacing:.3px}
  .field{position:absolute;height:21px;border:1px solid var(--field-line);font-size:11px;font-weight:300;color:var(--gold);display:flex;align-items:center;justify-content:center;letter-spacing:.3px}
  .field.plain{border:none;justify-content:flex-start;font-size:13px}
  .select{position:absolute;height:21px;width:84px;border:1px solid var(--field-line);font-size:5.5px;font-weight:600;color:var(--gold);display:flex;align-items:center;justify-content:space-between;padding:0 6px 0 8px}
  .check-btn{position:absolute;left:833px;top:166px;width:77px;height:103px;background:var(--gold);color:#fff;font-size:8px;font-weight:700;line-height:10px;display:flex;align-items:center;padding-left:13px}

  .listing{position:absolute;left:316px;top:312px;display:grid;grid-template-columns:184px 184px 185px;grid-auto-rows:245px;column-gap:15px;row-gap:24px}
  .need-card{background:#fff;padding:4px}
  .need-inner{border:1.5px solid var(--gold);height:100%;padding:10px 16px 0 21px}
  .need-inner h2{font-size:16.5px;line-height:20px;font-weight:700;color:var(--gold);margin-bottom:23px}
  .need-inner h3{font-size:7.5px;font-weight:700;color:var(--gold);margin-bottom:5px;margin-left:-3px}
  .need-inner p{font-size:6.8px;line-height:8.5px;color:var(--ink);margin-bottom:17px;margin-left:-3px}

  .apt{position:relative;background:#fff;display:flex;flex-direction:column}
  .apt.raised{box-shadow:0 6px 14px rgba(0,0,0,.18)}
  .apt-photo{height:154px}
  .apt-info{height:65px;background:#f4f4f4;padding:9px 14px 0}
  .apt-info h4{font-size:7.6px;line-height:9.6px;font-weight:700;color:var(--ink)}
  .apt-info p{font-size:7px;line-height:12.8px;color:var(--ink-soft)}
  .apt-info h4+p{margin-top:5px}
  .apt-actions{height:26px;display:flex}
  .apt-actions span{flex:1;display:flex;align-items:center;justify-content:center;font-size:7px;font-weight:700;letter-spacing:.3px}
  .btn-details{background:var(--gold);color:#fff}
  .btn-book{background:#fff;color:var(--gold)}
  .price{position:absolute;left:0;top:32px;height:16px;padding:0 12px 0 6px;background:var(--gold);color:#fff;font-size:7px;font-weight:700;display:flex;align-items:center;border-radius:0 9px 9px 0}

  .tone-a{background:linear-gradient(160deg,#5b5b5d,#8b8b89 55%,#3f3e3d)}
  .tone-b{background:linear-gradient(180deg,#e7e2d8,#c9bca6 60%,#8c8272)}
  .tone-c{background:linear-gradient(180deg,#ececeb,#d5d2cc 60%,#a9a49c)}
  .tone-d{background:linear-gradient(180deg,#dcdcdc,#a9a8a5 55%,#6d6865)}
  .tone-e{background:linear-gradient(180deg,#9aa5b2,#7f7e80 55%,#e4e2e2)}
  .tone-f{background:linear-gradient(180deg,#eef1f3,#c5cbd0 55%,#6b6663)}
  .tone-g{background:linear-gradient(180deg,#6a5343,#8e6e55 55%,#7b2a22)}
  .tone-h{background:linear-gradient(180deg,#4a3a2d,#7e6447 55%,#2d2520)}

  .site-footer{position:absolute;left:238px;top:1144px;width:738px;height:56px;background:#fff;display:flex;align-items:center;padding:0 38px 0 46px;font-size:9px;color:var(--ink)}
  .site-footer .item{display:flex;align-items:center;gap:8px;margin-right:18px}
  .site-footer .lang{font-size:7px;font-weight:700}
  .site-footer .copy{margin-left:auto;font-size:7px;font-weight:700}
</style>
</head>
<body>
  <div class="page"></div>

  <div class="hero-photo" role="img" aria-label="Photo of a bright luxury apartment living room with panoramic windows"></div>

  <aside class="sidebar">
    <div class="brand">
      <span class="brand-mark"></span>
      <span class="brand-name">BELVUE APARTMENTS</span>
    </div>
    <ul class="main-nav">
      <li class="active">APARTMENTS</li>
      <li>LOCATION</li>
      <li>SERVICES</li>
      <li>GALLERY</li>
      <li>NEWS</li>
      <li>EXCLUSIVE OFFERS &amp; TOURS</li>
      <li>FOR FAMILIES</li>
      <li>CONTACT US</li>
    </ul>
    <div class="sidebar-heading">OUR HOSPITALITY</div>
  </aside>

  <div class="discover">DISCOVER PRAGUE</div>

  <section class="booking-head">
    <h1>BEING HOME<br>IN PRAGUE</h1>
    <div class="label">INSTANT BOOK</div>
  </section>
  <form class="booking-form">
    <div class="field-label" style="left:13px;top:20px">CHECK-IN</div>
    <div class="field" style="left:12px;top:28px;width:84px">21 DEC 2017</div>
    <div class="field-label" style="left:104px;top:19px">STAY FOR</div>
    <div class="field" style="left:103px;top:28px;width:84px">13 DAYS</div>
    <div class="field-label" style="left:194px;top:20px">CHECK-OUT</div>
    <div class="field plain" style="left:193px;top:28px;width:90px">JAN 04 2018</div>
    <div class="field-label" style="left:13px;top:63px">GUEST DETAIL</div>
    <div class="select" style="left:12px;top:70px">ADULTS<svg width="9" height="6" viewBox="0 0 9 6"><path d="M1 1l3.5 3.5L8 1" fill="none" stroke="#e6bf36" stroke-width="1.2"/></svg></div>
    <div class="select" style="left:103px;top:70px">CHILDREN<svg width="9" height="6" viewBox="0 0 9 6"><path d="M1 1l3.5 3.5L8 1" fill="none" stroke="#e6bf36" stroke-width="1.2"/></svg></div>
    <div class="select" style="left:194px;top:70px">INFANTS<svg width="9" height="6" viewBox="0 0 9 6"><path d="M1 1l3.5 3.5L8 1" fill="none" stroke="#e6bf36" stroke-width="1.2"/></svg></div>
  </form>
  <div class="check-btn">CHECK<br>AVAILABILITY</div>

  <main class="listing">
    <div class="need-card">
      <div class="need-inner">
        <h2>NEED TO<br>KNOW</h2>
        <h3>APARTMENTS</h3>
        <p>Also available to rent all the apartments together for companies or larger group</p>
        <h3>CHECK-OUT</h3>
        <p>12 Noon<br>Earliest Check in 3 PM<br>both are flexible by arrangement</p>
        <h3>RATES</h3>
        <p>Prices from 150 USD including tax</p>
      </div>
    </div>

    <article class="apt raised">
      <div class="apt-photo tone-a" role="img" aria-label="Photo of a dark modern living room with shelving and lounge chair"></div>
      <span class="price">FROM $ 150</span>
      <div class="apt-info"><h4>BRAND NEW LUXURY LIVING<br>STUNNING CONTEMPORARY DESIGN</h4><p>1 Bedroom<br>MAX 4 People</p></div>
      <div class="apt-actions"><span class="btn-details">DETAILS</span><span class="btn-book">BOOK NOW</span></div>
    </article>

    <article class="apt">
      <div class="apt-photo tone-b" role="img" aria-label="Photo of a tall-windowed room with white curtains"></div>
      <span class="price">FROM $ 150</span>
      <div class="apt-info"><h4>BRAND NEW LUXURY LIVING<br>STUNNING CONTEMPORARY DESIGN</h4><p>1 Bedroom<br>MAX 4 People</p></div>
      <div class="apt-actions"><span class="btn-details">DETAILS</span><span class="btn-book">BOOK NOW</span></div>
    </article>

    <article class="apt">
      <div class="apt-photo tone-c" role="img" aria-label="Photo of a light living room with sofa and window"></div>
      <span class="price">FROM $ 120</span>
      <div class="apt-info"><h4>BRAND NEW LUXURY LIVING<br>STUNNING CONTEMPORARY DESIGN</h4><p>1 Bedroom<br>MAX 4 People</p></div>
      <div class="apt-actions"><span class="btn-details">DETAILS</span><span class="btn-book">BOOK NOW</span></div>
    </article>

    <article class="apt">
      <div class="apt-photo tone-d" role="img" aria-label="Photo of a grey lounge with fireplace and wall TV"></div>
      <span class="price">FROM $ 120</span>
      <div class="apt-info"><h4>BRAND NEW LUXURY LIVING<br>STUNNING CONTEMPORARY DESIGN</h4><p>1 Bedroom<br>MAX 4 People</p></div>
      <div class="apt-actions"><span class="btn-details">DETAILS</span><span class="btn-book">BOOK NOW</span></div>
    </article>

    <article class="apt">
      <div class="apt-photo tone-e" role="img" aria-label="Photo of a bedroom with white bed and patterned curtains"></div>
      <span class="price">FROM $ 120</span>
      <div class="apt-info"><h4>BRAND NEW LUXURY LIVING<br>STUNNING CONTEMPORARY DESIGN</h4><p>1 Bedroom<br>MAX 4 People</p></div>
      <div class="apt-actions"><span class="btn-details">DETAILS</span><span class="btn-book">BOOK NOW</span></div>
    </article>

    <article class="apt">
      <div class="apt-photo tone-f" role="img" aria-label="Photo of a living room with city view through large windows"></div>
      <span class="price">FROM $ 120</span>
      <div class="apt-info"><h4>BRAND NEW LUXURY LIVING<br>STUNNING CONTEMPORARY DESIGN</h4><p>1 Bedroom<br>MAX 4 People</p></div>
      <div class="apt-actions"><span class="btn-details">DETAILS</span><span class="btn-book">BOOK NOW</span></div>
    </article>

    <article class="apt">
      <div class="apt-photo tone-g" role="img" aria-label="Photo of a warm lounge with crystal chandelier and red sofa"></div>
      <span class="price">FROM $ 120</span>
      <div class="apt-info"><h4>BRAND NEW LUXURY LIVING<br>STUNNING CONTEMPORARY DESIGN</h4><p>1 Bedroom<br>MAX 4 People</p></div>
      <div class="apt-actions"><span class="btn-details">DETAILS</span><span class="btn-book">BOOK NOW</span></div>
    </article>

    <article class="apt">
      <div class="apt-photo tone-h" role="img" aria-label="Photo of a classic wood-panelled salon with chandeliers"></div>
      <span class="price">FROM $ 120</span>
      <div class="apt-info"><h4>BRAND NEW LUXURY LIVING<br>STUNNING CONTEMPORARY DESIGN</h4><p>1 Bedroom<br>MAX 4 People</p></div>
      <div class="apt-actions"><span class="btn-details">DETAILS</span><span class="btn-book">BOOK NOW</span></div>
    </article>
  </main>

  <footer class="site-footer">
    <div class="item lang">
      <svg width="11" height="11" viewBox="0 0 12 12" fill="none" stroke="#222" stroke-width="1"><circle cx="6" cy="6" r="5"/><ellipse cx="6" cy="6" rx="2.2" ry="5"/><path d="M1 6h10"/></svg>
      LANGUAGE : ENGLISH
    </div>
    <div class="item">
      <svg width="11" height="9" viewBox="0 0 12 9" fill="none" stroke="#222" stroke-width="1"><rect x=".5" y=".5" width="11" height="8"/><path d="M.5 .5L6 5l5.5-4.5"/></svg>
      reservation@belvuestays.com
    </div>
    <div class="item">
      <svg width="10" height="10" viewBox="0 0 10 10"><path d="M2.2.6l1.6 2.2-.9 1.2c.6 1.2 1.6 2.2 2.9 2.9l1.2-.9 2.2 1.6-.9 1.8C4.8 9.2.8 5.2.4 1.5z" fill="#222"/></svg>
      420-555-010-214
    </div>
    <div class="copy">© BELVUE 2017</div>
  </footer>
</body>
</html>
```